Bramwell Business Card Design

hello,
we are looking for a business card design for our Fintech Company. We are credit card processing company that is also expanding in to the crypto market. We will be focusing on crypto processing, with a crypto wallet and crypto exchange. We like the purple in the logo. We want something modern and sophisticated but at the same time simple and trust worthy to work with banks.

Industry/Entity Type

Fintech

Logo Text

Bramwell

```html
<!DOCTYPE html>
<html lang="en">
<head>
<meta charset="utf-8">
<title>Bramwell Business Card</title>
<link href="https://fonts.googleapis.com/css2?family=Arimo:wght@400;700&display=swap" rel="stylesheet">
<style>
  :root {
    --backdrop: #e4e4e2;
    --card-white: #ffffff;
    --card-dark: #2e2e2e;
    --brand-navy: #1e2d52;
    --brand-purple: #4f3f9e;
    --text-grey: #3a3a3a;
    --rule-grey: #6a6a6a;
    --emboss-grey: #474747;
  }
  * { box-sizing: border-box; margin: 0; padding: 0; }
  html, body {
    width: 1200px; height: 801px; overflow: hidden;
    background: var(--backdrop);
    font-family: "Arimo", Arial, sans-serif;
  }
  .stage {
    position: relative; width: 1200px; height: 801px;
    display: flex; align-items: center; justify-content: center; gap: 50px;
  }
  .card {
    position: relative; width: 520px; height: 298px;
    border-bottom: 4px solid var(--brand-purple);
    box-shadow: 0 10px 24px rgba(0,0,0,0.12);
  }
  .card--front { background: var(--card-white); display: flex; align-items: center; }
  .card--back { background: var(--card-dark); display: flex; align-items: center; justify-content: center; }

  .brand-name {
    font-weight: 700; letter-spacing: -2px; line-height: 1;
  }
  .card--front .brand-name {
    color: var(--brand-navy); font-size: 50px;
    width: 262px; text-align: center;
  }
  .card--back .brand-name { color: var(--emboss-grey); font-size: 84px; }

  .divider {
    width: 1px; height: 180px; background: var(--rule-grey);
  }
  .details { padding-left: 26px; color: var(--text-grey); }
  .person-name {
    color: var(--brand-purple); font-weight: 700; font-size: 19px;
    letter-spacing: 0.5px; text-transform: uppercase;
  }
  .person-role { font-size: 13px; margin-top: 3px; }
  .address { font-size: 13px; line-height: 1.35; margin-top: 14px; }
  .contact-list { list-style: none; margin-top: 14px; font-size: 13px; line-height: 1.45; }
  .contact-list li { display: flex; align-items: center; gap: 8px; }
  .contact-icon { width: 11px; height: 11px; flex: none; }
</style>
</head>
<body>
<main class="stage">
  <section class="card card--front" aria-label="Business card front">
    <div class="brand-name">Bramwell</div>
    <div class="divider"></div>
    <div class="details">
      <h1 class="person-name">Elliot Marsh</h1>
      <p class="person-role">Manager</p>
      <p class="address">Your address, city<br>state, ZIP 0000</p>
      <ul class="contact-list">
        <li>
          <svg class="contact-icon" viewBox="0 0 12 12" aria-hidden="true"><path d="M3 1 L5 3.5 L4 5 Q5 7 7 8 L8.5 7 L11 9 L9.5 11 Q4 10.5 1 3 Z" fill="var(--brand-purple)"/></svg>
          555-204-7316
        </li>
        <li>
          <svg class="contact-icon" viewBox="0 0 12 12" aria-hidden="true"><rect x="1" y="2.5" width="10" height="7" fill="none" stroke="var(--brand-purple)" stroke-width="1.2"/><path d="M1 2.5 L6 6.5 L11 2.5" fill="none" stroke="var(--brand-purple)" stroke-width="1.2"/></svg>
          youremail@mailbox.com
        </li>
        <li>
          <svg class="contact-icon" viewBox="0 0 12 12" aria-hidden="true"><circle cx="6" cy="6" r="5" fill="var(--brand-purple)"/><path d="M1 6 H11 M6 1 V11 M2 3.5 H10 M2 8.5 H10" stroke="#fff" stroke-width="0.6" fill="none"/><ellipse cx="6" cy="6" rx="2.3" ry="5" fill="none" stroke="#fff" stroke-width="0.6"/></svg>
          www.yourwebsite.com
        </li>
      </ul>
    </div>
  </section>

  <section class="card card--back" aria-label="Business card back">
    <div class="brand-name">Bramwell</div>
  </section>
</main>
</body>
</html>
```